BRIGHTWAVE DENTAL *

please see attached.

Target Market(s)

Adults 18-60

Contact Information for Business Card

Website: brightwavedentalqz.com
Phone number 555 304 7726 email: brightwavedentalqz@mailvex.com
Address:417 S. Kellim rd
Suite#24, TX70000
Dr. Elias Varno, DDS

Font styles to use
Sans Serif

Requirements
Must have
• Logo, phone number website, doctor,
• 's name

```html
<!DOCTYPE html>
<html lang="en">
<head>
<meta charset="utf-8">
<title>Brightwave Dental – Business Card</title>
<link href="https://fonts.googleapis.com/css2?family=Work+Sans:wght@300;400;500&display=swap" rel="stylesheet">
<style>
  :root {
    --backdrop: #dcdcdc;
    --navy: #141d33;
    --navy-light: #1f2b47;
    --teal: #1a8a9e;
    --ink: #3a3a3a;
    --muted: #6b6b6b;
    --paper: #ffffff;
    --rule: #7a7a7a;
  }
  * { margin: 0; padding: 0; box-sizing: border-box; }
  html, body { width: 1200px; height: 930px; overflow: hidden; }
  body {
    background: var(--backdrop);
    font-family: "Work Sans", sans-serif;
    position: relative;
  }
  .card {
    position: absolute;
    width: 520px;
    height: 300px;
    border-radius: 22px;
    overflow: hidden;
    box-shadow: 0 6px 18px rgba(0,0,0,0.18);
  }
  .brand { display: flex; align-items: center; gap: 14px; }
  .brand-dot {
    width: 34px; height: 34px; border-radius: 50%;
    border: 1.5px solid currentColor; flex: none;
  }
  .brand-name { font-weight: 300; letter-spacing: 3px; white-space: nowrap; }

  /* Front */
  .card--front {
    left: 90px; top: 100px;
    background: linear-gradient(135deg, var(--navy-light), var(--navy) 55%);
    display: flex; align-items: center; justify-content: center;
  }
  .card--front .brand { color: var(--paper); }
  .card--front .brand-name { font-size: 28px; }

  /* Back */
  .card--back { left: 590px; top: 530px; background: var(--paper); }
  .card__band {
    position: absolute; left: 0; top: 0; width: 100%; height: 84px;
    background: var(--navy);
  }
  .card__stripe {
    position: absolute; left: 0; top: 88px; width: 100%; height: 4px;
    background: var(--teal);
  }
  .card--back .brand {
    position: absolute; left: 28px; top: 148px;
    color: var(--ink); gap: 10px;
  }
  .card--back .brand-dot { width: 26px; height: 26px; }
  .card--back .brand-name { font-size: 18px; letter-spacing: 2px; }
  .doctor { position: absolute; right: 26px; top: 110px; text-align: right; }
  .doctor__name { color: var(--teal); font-weight: 500; font-size: 21px; letter-spacing: 0.5px; }
  .doctor__title {
    color: var(--muted); font-size: 10px; letter-spacing: 1px;
    border-top: 1px solid var(--rule); margin-top: 3px; padding-top: 2px;
    width: 210px; margin-left: auto;
  }
  .address {
    position: absolute; right: 26px; top: 162px; text-align: right;
    color: var(--ink); font-size: 11.5px; line-height: 1.45; letter-spacing: 0.8px;
  }
  .divider {
    position: absolute; left: 28px; right: 26px; top: 206px;
    border-top: 1px solid var(--rule);
  }
  .contacts {
    position: absolute; left: 28px; top: 216px; list-style: none;
    color: var(--ink); font-size: 11.5px; line-height: 1.55; letter-spacing: 0.6px;
  }
  .contacts li { display: flex; align-items: center; gap: 7px; }
  .contacts svg { width: 9px; height: 9px; fill: none; stroke: var(--teal); stroke-width: 1.6; flex: none; }
  .contacts .accent { color: var(--teal); }
</style>
</head>
<body>
  <section class="card card--front">
    <div class="brand">
      <span class="brand-dot"></span>
      <span class="brand-name">BRIGHTWAVE DENTAL</span>
    </div>
  </section>

  <section class="card card--back">
    <div class="card__band"></div>
    <div class="card__stripe"></div>

    <div class="brand">
      <span class="brand-dot"></span>
      <span class="brand-name">BRIGHTWAVE DENTAL</span>
    </div>

    <div class="doctor">
      <div class="doctor__name">DR. ELIAS VARNO</div>
      <div class="doctor__title">DDS</div>
    </div>

    <div class="address">417 S. KELLIM RD<br>Suite#24, TX70000</div>

    <div class="divider"></div>

    <ul class="contacts">
      <li><svg viewBox="0 0 10 10"><path d="M2,1 L4,1 L4.5,3 L3.5,4 Q4.5,6 6,6.5 L7,5.5 L9,6 L9,8 Q5,9 1.5,5 Q1,3 2,1 Z"/></svg><span>555 304 7726</span></li>
      <li><svg viewBox="0 0 10 10"><rect x="1" y="2" width="8" height="6"/><path d="M1,2 L5,5.5 L9,2"/></svg><span>info@brightwavedentalqz.com</span></li>
      <li><svg viewBox="0 0 10 10"><circle cx="5" cy="5" r="4"/><path d="M1,5 H9 M5,1 Q2.5,5 5,9 M5,1 Q7.5,5 5,9"/></svg><span>www.<span class="accent">brightwavedentalqz</span>.com</span></li>
    </ul>
  </section>
</body>
</html>
```